Business Card Design with new logo

Dorian Pelleway 4172
E 118th St Tambry, KS 66999
Cell: 217-555-0193
pellewayrestoration@mailvane.test

Classic Car Restoration Services Buy Sell Trade Consign

Dorian Pelleway 4172
Cell: 217-555-0193

```html
<!DOCTYPE html>
<html lang="en">
<head>
<meta charset="UTF-8">
<title>Pelleway Restoration LLC – Business Card</title>
<link rel="stylesheet" href="https://fonts.googleapis.com/css2?family=Roboto:wght@400;500;700&display=swap">
<style>
  :root {
    --page-bg: #ecebe8;
    --card-bg: #ffffff;
    --brand-red: #e0262b;
    --brand-navy: #1f2a36;
    --divider-blue: #3f4aa6;
    --text-dark: #3a3a3a;
    --text-grey: #9a9a9a;
  }
  * { margin: 0; padding: 0; box-sizing: border-box; }
  html, body {
    width: 1200px; height: 800px; overflow: hidden;
    background: var(--page-bg);
    font-family: "Roboto", Arial, sans-serif;
  }
  .sheet {
    width: 1200px; height: 800px;
    display: flex; align-items: center; justify-content: center; gap: 40px;
  }
  .card {
    position: relative;
    width: 540px; height: 310px;
    background: var(--card-bg);
    box-shadow: 0 6px 18px rgba(0,0,0,0.12);
    overflow: hidden;
  }

  /* Brand wordmark */
  .brand { display: flex; flex-direction: column; align-items: center; }
  .brand-dot {
    width: 40px; height: 40px; border-radius: 50%;
    background: var(--brand-red); margin-bottom: 16px;
  }
  .brand-name {
    font-weight: 700; color: var(--brand-navy);
    text-transform: uppercase; text-align: center; line-height: 1.2;
  }

  /* Contact side */
  .card--contact .brand {
    position: absolute; left: 20px; top: 86px; width: 210px;
  }
  .card--contact .brand-dot { width: 30px; height: 30px; margin-bottom: 12px; }
  .card--contact .brand-name { font-size: 21px; letter-spacing: 1px; }
  .card--contact .brand-name span { display: block; font-size: 12px; letter-spacing: 4px; }
  .divider {
    position: absolute; left: 248px; top: 34px;
    width: 2px; height: 190px; background: var(--divider-blue);
  }
  .details { position: absolute; left: 270px; top: 34px; width: 260px; }
  .details .person {
    font-size: 17px; font-weight: 700; color: var(--brand-red);
    text-transform: uppercase; letter-spacing: 0.3px;
  }
  .details .house-number { font-size: 13px; color: var(--text-grey); margin-top: 2px; }
  .contact-line {
    display: flex; align-items: center; gap: 8px;
    font-size: 12px; color: var(--text-dark); margin-top: 8px;
  }
  .contact-line svg { width: 13px; height: 13px; flex: none; }
  .contact-line:first-of-type { margin-top: 10px; }
  .address { font-size: 13px; color: var(--text-dark); line-height: 1.6; margin-top: 34px; }
  .rule-pair { position: absolute; }
  .rule-pair i { display: block; background: var(--brand-red); }
  .rule-pair i + i { margin-top: 4px; }
  .rule-pair--right { right: 44px; top: 218px; width: 200px; }
  .rule-pair--right i { height: 2px; }
  .rule-pair--right i + i { height: 4px; }
  .rule-pair--left { left: 130px; top: 268px; width: 110px; }
  .rule-pair--left i { height: 2px; }
  .rule-pair--left i + i { height: 5px; }

  /* Brand side */
  .card--logo { display: flex; align-items: center; justify-content: center; }
  .card--logo .brand-dot { width: 56px; height: 56px; margin-bottom: 24px; }
  .card--logo .brand-name { font-size: 42px; letter-spacing: 2px; }
  .card--logo .brand-name span { display: block; font-size: 20px; letter-spacing: 8px; margin-top: 6px; }
</style>
</head>
<body>
  <main class="sheet">
    <section class="card card--contact" aria-label="Business card, contact side">
      <div class="brand">
        <div class="brand-dot"></div>
        <div class="brand-name">Pelleway<span>Restoration LLC</span></div>
      </div>
      <div class="divider"></div>
      <div class="details">
        <p class="person">Dorian Pelleway</p>
        <p class="house-number">4172</p>
        <p class="contact-line">
          <svg viewBox="0 0 16 16" aria-hidden="true"><path fill="var(--brand-red)" d="M4 1l2.5 3.5-1.6 1.6c.9 2 2.3 3.4 4.3 4.3l1.6-1.6L14.3 11 13 14.2C7 14 2 9 1.8 3z"/></svg>
          217-555-0193
        </p>
        <p class="contact-line">
          <svg viewBox="0 0 16 16" aria-hidden="true"><rect x="1" y="3" width="14" height="10" fill="var(--brand-red)"/><path d="M1 3l7 6 7-6" fill="none" stroke="#fff" stroke-width="1.3"/></svg>
          pellewayrestoration@mailvane.test
        </p>
        <p class="address">E 118th St Tambry,<br>KS 66999</p>
      </div>
      <div class="rule-pair rule-pair--right"><i></i><i></i></div>
      <div class="rule-pair rule-pair--left"><i></i><i></i></div>
    </section>

    <section class="card card--logo" aria-label="Business card, brand side">
      <div class="brand">
        <div class="brand-dot"></div>
        <div class="brand-name">Pelleway<span>Restoration LLC</span></div>
      </div>
    </section>
  </main>
</body>
</html>
```